Poster for company's 5 NORMS

Good Day,

My name is Rilo and I am working for Morvane & Tolbrick Offshore Pte Ltd. We are in the Marine and Offshore industry and based in Singapore.

I have to submit a few A-2 sized poster design samples reflecting our 5 norms to my boss in 40 hours time. So I need your help.

The 5 norms are: (1) Ownership, (2) Positive Mindset, (3) Actions, (4) Teamwork, (5) Honesty.

My company logo can be googled. The corporate colours of the company are blue and grey predominantly and white is occasionally used. But feel free to play with colours. No need to stick to grey, blue and white. The words and headers, you can play with colours too. This poster must be an attention grabber. You can make it look professional yet fun as well.

A few of the poster designs should be build based on the following:
a) 2 liner headers reading the following:
Line 1: Our Winning 5 Norms!
LIne 2: OWNing the P.A.T.H to Tier 1

b) Bottom centre - company's logo

c) Design 1: A winding road (limit to 2 turns) as background and the 5 norms spread vertically along the winding road.

d) Design 2: A circle divided into 5 equal segments and in each segment, the 5 norms.

You should consider highlighting for the initial letter (s) of each word (OWN, P, A, T, H) so that it will reemphasize Owning the Path. Also, attached is a design for the poster that we have on our walls now. I did not scan it properly but I would want a much much better poster.

Please feel free to be creative, especially for the other designs.

Thank you very much. Looking forward to see posters in my inbox.

Have a great day ahead,

Regards, Rilo

Hp: 65-93172548

Good Day,

I just attached a picture of our current poster. I did not scan it well, apologies for that. But we would want a much much better poster.

Thank you!

Hello guys,

I have attached a picture of the company's logo. You can also visit the link below to get the correct logo.

It should state "Morvane & Tolbrick Offshore".

Thanks.

https://www.quorvelsearch.example/search?q=morvane+and+tolbrick+offshore+logo&hl=en-SG&source=lnms&tbm=isch&sa=X&ei=Kp7WQrLMPdazqfht4hJ9Rf&ved=0DBlR_BVpBQ&biw=1366&bih=636&dpr=1

Target Market(s)

Internal stakeholders. Good if it can impress clients as well.

Industry/Entity Type

Industry

Font styles to use
Serif

```html
<!DOCTYPE html>
<html lang="en">
<head>
<meta charset="utf-8">
<title>Our Winning 5 Norms! OWNing the P.A.T.H. to Tier I — Morvane &amp; Tolbrick Offshore</title>
<link rel="stylesheet" href="https://fonts.googleapis.com/css2?family=Orbitron:wght@400;500&family=Saira+Semi+Condensed:wght@600&display=swap">
<style>
  :root {
    --paper: #a9aaac;
    --paper-light: #bdbec0;
    --title-navy: #1c2a66;
    --petal: #1f2233;
    --petal-edge: #2f3349;
    --hands: #0f111b;
    --norm-text: #e6e7ea;
    --norm-initial: #8fb4ec;
    --brand-ink: #1d1d20;
  }
  * { margin: 0; padding: 0; box-sizing: border-box; }
  html, body { width: 849px; height: 1200px; overflow: hidden; background: var(--paper); }
  .poster {
    position: relative;
    width: 849px;
    height: 1200px;
    overflow: hidden;
    background: radial-gradient(ellipse at 50% 45%, var(--paper-light) 0%, var(--paper) 70%);
  }
  .kicker {
    position: absolute;
    top: 12px;
    left: 0;
    width: 100%;
    text-align: center;
    font-family: "Orbitron", sans-serif;
    font-weight: 500;
    font-size: 30px;
    line-height: 40px;
    letter-spacing: 2px;
    color: var(--title-navy);
  }
  .headline {
    position: absolute;
    top: 54px;
    left: 0;
    width: 100%;
    text-align: center;
    font-family: "Orbitron", sans-serif;
    font-weight: 400;
    font-size: 66px;
    line-height: 82px;
    color: var(--title-navy);
    letter-spacing: 1px;
  }
  .norms-flower { position: absolute; top: 0; left: 0; width: 849px; height: 1200px; }
  .petal { fill: var(--petal); stroke: var(--petal-edge); stroke-width: 2; }
  .hands-area { fill: none; stroke: var(--hands); stroke-width: 80; opacity: 0.35; }
  .norm-label {
    font-family: "Saira Semi Condensed", "Arial Narrow", sans-serif;
    font-weight: 600;
    font-size: 52px;
    letter-spacing: 2px;
    fill: var(--norm-text);
  }
  .norm-initial { fill: var(--norm-initial); }
  .brand {
    position: absolute;
    top: 1022px;
    left: 0;
    width: 100%;
    display: flex;
    justify-content: center;
    align-items: center;
    gap: 26px;
  }
  .brand-dot { width: 120px; height: 120px; border-radius: 50%; background: var(--brand-ink); }
  .brand-name {
    font-family: "Orbitron", sans-serif;
    font-weight: 400;
    font-size: 24px;
    line-height: 34px;
    color: var(--brand-ink);
    letter-spacing: 1px;
  }
</style>
</head>
<body>
<main class="poster">
  <p class="kicker">Our Winning 5 Norms!</p>
  <h1 class="headline">OWNing the<br>P.A.T.H. to Tier I</h1>

  <svg class="norms-flower" viewBox="0 0 849 1200" xmlns="http://www.w3.org/2000/svg">
    <defs>
      <path id="arc-ownership" d="M425,548 A128,128 0 1 1 425,292 A128,128 0 1 1 425,548"/>
      <path id="arc-action" d="M512.5,611.6 A128,128 0 1 1 755.9,532.4 A128,128 0 1 1 512.5,611.6"/>
      <path id="arc-honesty" d="M479.1,714.4 A128,128 0 1 1 629.5,921.6 A128,128 0 1 1 479.1,714.4"/>
      <path id="arc-teamwork" d="M370.9,714.4 A128,128 0 1 1 220.5,921.6 A128,128 0 1 1 370.9,714.4"/>
      <path id="arc-mindset" d="M337.5,611.6 A128,128 0 1 1 94.1,532.4 A128,128 0 1 1 337.5,611.6"/>
    </defs>

    <g class="petals">
      <circle class="petal" cx="425" cy="420" r="174"/>
      <circle class="petal" cx="634.2" cy="572" r="174"/>
      <circle class="petal" cx="554.3" cy="818" r="174"/>
      <circle class="petal" cx="295.7" cy="818" r="174"/>
      <circle class="petal" cx="215.8" cy="572" r="174"/>
    </g>

    <circle class="hands-area" cx="425" cy="640" r="120" role="img" aria-label="Five hands reaching in to meet at the centre"/>

    <g class="norm-labels">
      <text class="norm-label"><textPath href="#arc-ownership" startOffset="50%" text-anchor="middle"><tspan class="norm-initial">Own</tspan>ership</textPath></text>
      <text class="norm-label"><textPath href="#arc-action" startOffset="50%" text-anchor="middle"><tspan class="norm-initial">A</tspan>ction</textPath></text>
      <text class="norm-label"><textPath href="#arc-honesty" startOffset="50%" text-anchor="middle"><tspan class="norm-initial">H</tspan>onesty</textPath></text>
      <text class="norm-label"><textPath href="#arc-teamwork" startOffset="50%" text-anchor="middle"><tspan class="norm-initial">T</tspan>eamwork</textPath></text>
      <text class="norm-label"><textPath href="#arc-mindset" startOffset="50%" text-anchor="middle" textLength="400" lengthAdjust="spacingAndGlyphs"><tspan class="norm-initial">P</tspan>ositive Mindset</textPath></text>
    </g>
  </svg>

  <footer class="brand">
    <span class="brand-dot" aria-hidden="true"></span>
    <p class="brand-name">MORVANE &amp; TOLBRICK<br>OFFSHORE</p>
  </footer>
</main>
</body>
</html>
```